3 pages of UI design for AdTech Startup

We need 3 pages of UI design for a new AdTech company located in Seattle called KELVRA Systems.

We put digital, mobile billboards on college campuses throughout the country. This design project involves our back-end customer dashboard.

Page 1- Dashboard home page
page 2- Manage ads screen (see File 3 below for the screenshot of our current design). Please match the design of all 3 screens so there is consistency
page 3-Detailed Zone screen (see file 16 below). This page looks similar to the first page but gives a more detailed overview and a larger map.

The features and functionality are already built but we are lacking an aesthetically pleasing and slick design. Looking for someone who can match our website look to this new dashboard space. Our company reflects modern, clean, elegant design that is straight-forward and user friendly (main inspiration is TROVI, we love their design and feel).

Target Market(s)

-Local business owner, marketing directors, and national advertising and marketing agencies

Industry/Entity Type

Advertising

Number of Pages Required

3 page

Font styles to use
Other font styles liked:
• Proxima Nova- Thin for body text, Light for title

Colors
85cae6
33a6d7
0292cd
ffffff

Requirements
Nice to have
• Please include enough detail so that my developer can look at the design you come up with and translate it to html. Please include spacing, fonts, color numbers. My developer is going to look at your creation and recreate it in html format

```html
<!DOCTYPE html>
<html lang="en">
<head>
<meta charset="utf-8">
<title>KELVRA Systems – Insights Summary</title>
<link href="https://fonts.googleapis.com/css2?family=Montserrat:wght@300;400;600&family=Open+Sans:wght@300;400&display=swap" rel="stylesheet">
<style>
:root{
  --black:#000;
  --brand:#3fb4dd;
  --brand-dark:#0292cd;
  --line:#85cae6;
  --white:#fff;
  --tab-grey:#7a7a7a;
  --zone-a:#a9a9a9;
  --zone-b:#8f8f8f;
  --text-dark:#333;
  --axis:#777;
  --point:#1b2a3a;
  --area:#f1f1f4;
}
*{margin:0;padding:0;box-sizing:border-box}
html,body{width:902px;height:1200px;overflow:hidden;background:var(--white)}
body{position:relative;font-family:"Open Sans",sans-serif;color:var(--text-dark)}
.abs{position:absolute}

/* top bar */
.topbar{left:0;top:0;width:902px;height:40px;background:var(--black);color:var(--white)}
.menu-icon{left:43px;top:13px}
.brand-mark{left:0;width:902px;top:11px;text-align:center;font-family:"Montserrat",sans-serif;font-weight:300;font-size:15px;letter-spacing:3px;color:var(--brand)}
.search-icon{left:682px;top:14px}
.avatar{left:715px;top:11px;width:18px;height:18px;border-radius:50%;background:#8a8a8a}
.avatar-badge{left:726px;top:8px;width:9px;height:9px;border-radius:50%;background:var(--brand);font-size:6px;line-height:9px;text-align:center}
.user-name{left:742px;top:14px;font-size:9px;color:#ddd}
.caret{left:795px;top:18px;width:0;height:0;border-left:3px solid transparent;border-right:3px solid transparent;border-top:3px solid #aaa}
.league-name{left:812px;top:13px;font-size:11px;font-weight:400;color:var(--white)}

/* summary band */
.summary{left:0;top:40px;width:902px;height:75px;background:var(--brand);color:var(--white)}
.summary-title{left:39px;top:13px;font-size:19px;font-weight:300}
.tabs{left:40px;top:53px;display:flex;font-size:12px;font-weight:300}
.tab{height:22px;line-height:22px;text-align:center;background:var(--tab-grey);color:#eee}
.tab.active{background:var(--white);color:#888}
.tab.active::after{content:"";display:inline-block;margin-left:6px;vertical-align:2px;border-left:3px solid transparent;border-right:3px solid transparent;border-bottom:4px solid #888}
.stat-label{font-family:"Montserrat",sans-serif;font-size:7px;letter-spacing:2px}
.stat-value{font-family:"Montserrat",sans-serif;font-size:11px;letter-spacing:3px;margin-top:1px}

/* chart */
.date-range{left:78px;top:165px;font-family:"Montserrat",sans-serif;font-size:9px;letter-spacing:2px;color:#444}
.chart{left:0;top:115px}

/* zones */
.zones-head{left:0;top:573px;width:902px;height:24px;background:var(--black);color:var(--white);text-align:center;font-size:17px;line-height:24px;border-bottom:2px solid var(--white);height:26px}
.zone{left:0;width:902px}
.zone-a{top:599px;height:286px;background:var(--zone-a)}
.zone-b{top:885px;height:277px;background:var(--zone-b)}
.zone-name{left:57px;top:6px;font-size:18px;color:var(--white);font-weight:400}
.panel-head{height:24px;line-height:24px;background:var(--brand);color:var(--white);font-size:10px;text-align:center}
.ad-card{left:56px;top:34px;width:324px}
.ad-photo{height:186px;background:linear-gradient(160deg,#2a1a1e 0%,#5a1f24 45%,#1c1618 100%)}
.manage-ads{height:19px;line-height:19px;background:var(--brand);color:var(--white);text-align:center;font-size:11px;font-weight:300}
.map-card{left:393px;top:34px;width:325px}
.map-view{height:205px;background:linear-gradient(135deg,#3f5a2e 0%,#5d6f45 50%,#41552f 100%);position:relative;border:1px solid var(--brand)}
.map-toggle{position:absolute;left:5px;top:5px;display:flex;background:var(--white);font-size:6px}
.map-toggle span{padding:4px 5px}
.map-toggle .on{font-weight:400;color:#000}
.map-source{position:absolute;left:3px;bottom:2px;font-size:10px;color:var(--white)}
.perf-card{left:733px;top:34px;width:113px}
.perf-list{padding:18px 0 0 12px;color:var(--white)}
.perf-list .stat-value{margin-bottom:9px;font-size:12px}
.details-btn{position:absolute;left:0;width:113px;height:20px;line-height:20px;background:var(--brand);color:var(--white);text-align:center;font-size:11px;font-weight:300}

/* footer */
.footer{left:0;top:1162px;width:902px;height:38px;background:var(--black);color:var(--white)}
.footer-links{left:43px;top:13px;font-size:7px;line-height:10px}
.social{right:40px;top:13px;display:flex;gap:16px;font-size:10px}
</style>
</head>
<body>

<header class="abs topbar">
  <svg class="abs menu-icon" width="20" width="20" height="14" viewBox="0 0 20 14"><rect y="0" width="20" height="2" fill="#fff"/><rect y="6" width="20" height="2" fill="#fff"/><rect y="12" width="20" height="2" fill="#fff"/></svg>
  <div class="abs brand-mark">KELVRA</div>
  <svg class="abs search-icon" width="11" height="11" viewBox="0 0 11 11"><circle cx="4.5" cy="4.5" r="3.5" stroke="#fff" stroke-width="1.6" fill="none"/><line x1="7" y1="7" x2="10" y2="10" stroke="#fff" stroke-width="1.8"/></svg>
  <div class="abs avatar" role="img" aria-label="User avatar"></div>
  <div class="abs avatar-badge">2</div>
  <div class="abs user-name">Dana Whitlock</div>
  <div class="abs caret"></div>
  <div class="abs league-name">HOOPLEAGUE</div>
</header>

<section class="abs summary">
  <h1 class="abs summary-title">Insights Summary</h1>
  <nav class="abs tabs">
    <div class="tab" style="width:77px">Yearly</div>
    <div class="tab active" style="width:79px">Monthly</div>
    <div class="tab" style="width:74px">Daily</div>
  </nav>
  <div class="abs" style="left:552px;top:14px"><div class="stat-label">ROTATIONS</div><div class="stat-value">85</div></div>
  <div class="abs" style="left:707px;top:14px"><div class="stat-label">TIME</div><div class="stat-value">21.25 min</div></div>
  <div class="abs" style="left:552px;top:47px"><div class="stat-label">IMPRESSIONS</div><div class="stat-value">595</div></div>
  <div class="abs" style="left:707px;top:47px"><div class="stat-label">MILES</div><div class="stat-value">0.3 miles</div></div>
</section>

<div class="abs date-range">2016/01/01 - 2016/06/15</div>

<svg class="abs chart" width="902" height="458" viewBox="0 115 902 458" font-family="Open Sans, sans-serif">
  <polygon points="161,357 212,265 313,311 414,218 518,357 619,310 722,286 774,404 774,498 161,498" fill="var(--area)"/>
  <g stroke="#bbb" stroke-dasharray="2 3" stroke-width="0.8">
    <line x1="110" y1="218" x2="826" y2="218"/><line x1="110" y1="264" x2="826" y2="264"/>
    <line x1="110" y1="311" x2="826" y2="311"/><line x1="110" y1="357" x2="826" y2="357"/>
    <line x1="110" y1="404" x2="826" y2="404"/><line x1="110" y1="450" x2="826" y2="450"/>
    <line x1="211" y1="190" x2="211" y2="498"/><line x1="313" y1="190" x2="313" y2="498"/>
    <line x1="415" y1="190" x2="415" y2="498"/><line x1="517" y1="190" x2="517" y2="498"/>
    <line x1="619" y1="190" x2="619" y2="498"/><line x1="721" y1="190" x2="721" y2="498"/>
  </g>
  <g stroke="var(--line)" stroke-width="1.5">
    <line x1="110" y1="498" x2="826" y2="498"/>
    <line x1="110" y1="494" x2="110" y2="503"/><line x1="211" y1="494" x2="211" y2="503"/>
    <line x1="313" y1="494" x2="313" y2="503"/><line x1="415" y1="494" x2="415" y2="503"/>
    <line x1="517" y1="494" x2="517" y2="503"/><line x1="619" y1="494" x2="619" y2="503"/>
    <line x1="721" y1="494" x2="721" y2="503"/><line x1="826" y1="494" x2="826" y2="503"/>
  </g>
  <polyline points="161,357 212,265 313,311 414,218 518,357 619,310 722,286 774,404" fill="none" stroke="var(--line)" stroke-width="2.5"/>
  <g fill="#fff" stroke="var(--point)" stroke-width="2">
    <circle cx="161" cy="357" r="6.5"/><circle cx="212" cy="265" r="6.5"/><circle cx="313" cy="311" r="6.5"/>
    <circle cx="414" cy="218" r="6.5"/><circle cx="518" cy="357" r="6.5"/><circle cx="619" cy="310" r="6.5"/>
    <circle cx="722" cy="286" r="6.5"/><circle cx="774" cy="404" r="6.5"/>
  </g>
  <g fill="#777" font-size="17" font-weight="300">
    <text x="67" y="224">90</text><text x="67" y="317">60</text><text x="67" y="410">30</text>
  </g>
  <g fill="#888" font-size="12" font-weight="300" text-anchor="middle">
    <text x="161" y="526">JAN</text><text x="262" y="526">FEB</text><text x="366" y="526">MAR</text>
    <text x="466" y="526">APR</text><text x="570" y="526">MAY</text><text x="671" y="526">JUN</text><text x="774" y="526">JUL</text>
  </g>
</svg>

<div class="abs zones-head">ZONES</div>

<section class="abs zone zone-a">
  <h2 class="abs zone-name">Marlow's House</h2>
  <div class="abs ad-card">
    <div class="panel-head">Active Ad</div>
    <div class="ad-photo" role="img" aria-label="Active ad photo: basketball player dunking in an arena"></div>
    <div class="manage-ads">Manage Ads</div>
  </div>
  <div class="abs map-card">
    <div class="panel-head">Carrier Path</div>
    <div class="map-view" role="img" aria-label="Satellite map of the neighbourhood with the carrier path">
      <div class="map-toggle"><span>Map</span><span class="on">Satellite</span></div>
      <div class="map-source">Mapsource</div>
    </div>
  </div>
  <div class="abs perf-card">
    <div class="panel-head" style="height:23px;line-height:23px">Zone Performance</div>
    <div class="perf-list">
      <div class="stat-label">ROTATIONS</div><div class="stat-value">85</div>
      <div class="stat-label">IMPRESSIONS</div><div class="stat-value">595</div>
      <div class="stat-label" style="margin-top:6px">TIME</div><div class="stat-value">21.25 min</div>
      <div class="stat-label" style="margin-top:4px">MILES</div><div class="stat-value">0.3 miles</div>
    </div>
    <div class="details-btn" style="top:210px">Details</div>
  </div>
</section>

<section class="abs zone zone-b">
  <h2 class="abs zone-name">Campus Bites</h2>
  <div class="abs ad-card" style="top:37px">
    <div class="panel-head">Active Ad</div>
    <div class="ad-photo" role="img" aria-label="Active ad photo: basketball player dunking in an arena"></div>
    <div class="manage-ads">Manage Ads</div>
  </div>
  <div class="abs map-card" style="top:37px">
    <div class="panel-head">Carrier Path</div>
    <div class="map-view" role="img" aria-label="Satellite map of the neighbourhood with the carrier path">
      <div class="map-toggle"><span>Map</span><span class="on">Satellite</span></div>
      <div class="map-source">Mapsource</div>
    </div>
  </div>
  <div class="abs perf-card" style="top:37px">
    <div class="panel-head" style="height:23px;line-height:23px">Zone Performance</div>
    <div class="perf-list">
      <div class="stat-label">ROTATIONS</div><div class="stat-value">85</div>
      <div class="stat-label">IMPRESSIONS</div><div class="stat-value">595</div>
      <div class="stat-label" style="margin-top:6px">TIME</div><div class="stat-value">21.25 min</div>
      <div class="stat-label" style="margin-top:4px">MILES</div><div class="stat-value">0.3 miles</div>
    </div>
    <div class="details-btn" style="top:210px">Details</div>
  </div>
</section>

<footer class="abs footer">
  <div class="abs footer-links">Home | About | Products | Services | Contact<br>Privacy Policy | Terms of use</div>
  <div class="abs social"><span>Chirpr</span><span>Friendly</span><span>Picto</span></div>
</footer>

</body>
</html>
```